Business card design needed

We need a business card for a new business. We are called Little Tradies Wear, and we make replica kid size clothing, mainly hi vis shirts, work trousers and shorts. Our long term goal is to include clothing for numerous trades and professions, for our littlest Aussies. We would like a kid friendly card using navy blue, bright orange, bright yellow and bright pink. We haven't set up our web page yet because we want to base it on our final business card design.
Updates

Industry/Entity Type

Clothing

```html
<!DOCTYPE html>
<html lang="en">
<head>
<meta charset="utf-8">
<title>Little Tradies Wear – Business Card</title>
<link href="https://fonts.googleapis.com/css2?family=Questrial&display=swap" rel="stylesheet">
<style>
  :root {
    --backdrop: #e9e6e1;
    --navy-light: #2d3068;
    --navy-dark: #1e2155;
    --tab-navy: #2b2b4c;
    --yellow-light: #f0ea3c;
    --yellow-dark: #d5cb30;
    --accent-yellow: #ece33c;
    --card-shadow: rgba(0, 0, 0, 0.28);
  }
  * { margin: 0; padding: 0; box-sizing: border-box; }
  html, body {
    width: 1200px;
    height: 1181px;
    overflow: hidden;
    background: var(--backdrop);
    font-family: "Questrial", "Century Gothic", sans-serif;
  }
  .canvas { position: relative; width: 1200px; height: 1181px; }
  .card {
    position: absolute;
    left: 276px;
    width: 647px;
    height: 371px;
    border-radius: 22px;
    overflow: hidden;
    box-shadow: 0 6px 14px var(--card-shadow);
  }
  .card--front {
    top: 182px;
    background: radial-gradient(ellipse at 50% 40%, var(--navy-light) 0%, var(--navy-dark) 75%);
  }
  .card--back {
    top: 619px;
    background: radial-gradient(ellipse at 50% 45%, var(--yellow-light) 0%, var(--yellow-dark) 80%);
  }
  .brand-name {
    position: absolute;
    left: 0;
    right: 0;
    text-align: center;
    font-size: 27px;
    letter-spacing: 0.5px;
    white-space: nowrap;
  }
  .card--front .brand-name { top: 171px; color: var(--accent-yellow); }
  .card--back .brand-name { top: 170px; color: var(--tab-navy); }
  .tab {
    position: absolute;
    left: 215px;
    width: 217px;
    background: var(--tab-navy);
  }
  .tab--top {
    top: 0;
    height: 143px;
    border-radius: 0 0 24px 24px;
    display: flex;
    align-items: center;
    justify-content: center;
  }
  .tab--bottom {
    bottom: 0;
    height: 144px;
    border-radius: 24px 24px 0 0;
    text-align: center;
    color: var(--accent-yellow);
  }
  .contact__name { margin-top: 52px; font-size: 26px; line-height: 1; }
  .contact__role { margin-top: 3px; font-size: 10.5px; letter-spacing: 0.3px; }
  .contact__phone { margin-top: 12px; font-size: 10.5px; }
  .contact__email { margin-top: 2px; font-size: 10.5px; }
</style>
</head>
<body>
<main class="canvas">
  <section class="card card--front" aria-label="Card front">
    <p class="brand-name">Little Tradies Wear</p>
  </section>

  <section class="card card--back" aria-label="Card back">
    <div class="tab tab--top">
      <svg width="60" height="60" viewBox="0 0 60 60" aria-hidden="true">
        <circle cx="30" cy="30" r="26" fill="var(--accent-yellow)"/>
      </svg>
    </div>
    <p class="brand-name">Little Tradies Wear</p>
    <div class="tab tab--bottom">
      <p class="contact__name">Your Name</p>
      <p class="contact__role">Production Coordinator</p>
      <p class="contact__phone">1234-567-890</p>
      <p class="contact__email">yourname@company.com</p>
    </div>
  </section>
</main>
</body>
</html>
```